Fennick Executive Search - New Business Card Design Project

We are an executive search firm called Fennick Executive Search based in the UK. We require a custom design for a business card. We're looking to convey a professional service to executives for executive search recruitment services. In terms of colours, we like dark blues and grays (maybe even silver incorporated somewhere if we go for a foiled type of card) but we're open to your artistic flare. See our current logo in attachments. We are totally open on design so long as the design is slick and professional.
Updates

Thanks for all your contributions of various designs. I have to say the quality of work has been amazing which is going to make our job quite difficult in the coming days on making a decision. Thanks to you all that have taken the time to submit designs thus far. We'll keep on reviewing and try to narrow down our selection as soon as possible.

Target Market(s)

Executive Search

Industry/Entity Type

Recruitment

Contact Information for Business Card

Fennick Executive Search,
Exclusively Sourcing & Hiring Senior Leaders
Gordon Pellbury, Managing Director,
07823 906417
0117 486 7132
gordon@fennickexecutive.co.uk
fennickexecutive.co.uk
58 Lindmoor Court, Hatherley Road, Bristol, BS32 9QJ

Font styles to use
Sans Serif
Other font styles liked:
• Roboto (which is used in our logo)

Requirements
Must have
• Our logo (It has a subtle fade on it from #02071d at top to #333649 at bottom)
• The logo can be on one side or both sides
• Must be elegant and professional
• We have 2nd slogan CONSULT | INSPIRE | INNOVATE | DELIVER which can be incorporated into the card
Nice to have
• Use of blues and grey colours
• Compatible with similar styling to our website fennickexecutive.co.uk
Should not have
• Must not be overly brash
• Must not contain cartoon characters

```html
<!DOCTYPE html>
<html lang="en">
<head>
<meta charset="UTF-8">
<title>Fennick Executive Search – Business Card</title>
<link href="https://fonts.googleapis.com/css2?family=Open+Sans:ital,wght@0,400;0,600;1,400&display=swap" rel="stylesheet">
<style>
  :root {
    --page-bg: #e9eaee;
    --card-navy: #030a22;
    --text-white: #ffffff;
    --text-soft: #e6e8ef;
    --silver: #d3d5db;
  }
  html, body {
    margin: 0;
    padding: 0;
    width: 1200px;
    height: 900px;
    overflow: hidden;
    background: var(--page-bg);
    font-family: "Open Sans", Arial, sans-serif;
  }
  .business-card {
    position: absolute;
    left: 120px;
    top: 152px;
    width: 960px;
    height: 596px;
    background: var(--card-navy);
    color: var(--text-white);
    box-shadow: 0 18px 40px rgba(3, 10, 34, 0.25);
  }
  .holder-name {
    position: absolute;
    left: 55px;
    top: 78px;
    margin: 0;
    font-size: 35px;
    line-height: 44px;
    font-weight: 600;
    letter-spacing: 0.3px;
  }
  .holder-role {
    position: absolute;
    left: 55px;
    top: 124px;
    margin: 0;
    font-size: 24px;
    line-height: 32px;
    font-weight: 400;
    color: var(--text-soft);
  }
  .office-address {
    position: absolute;
    left: 58px;
    top: 270px;
    margin: 0;
    font-style: normal;
    font-size: 24px;
    line-height: 35px;
    color: var(--text-soft);
  }
  .contact-list {
    position: absolute;
    left: 58px;
    top: 388px;
    margin: 0;
    padding: 0;
    list-style: none;
    font-size: 24px;
    line-height: 35px;
    color: var(--text-soft);
  }
  .contact-item {
    display: flex;
    align-items: center;
    gap: 8px;
  }
  .contact-icon {
    width: 20px;
    height: 20px;
    fill: var(--text-white);
    flex: none;
  }
  .brand-block {
    position: absolute;
    left: 498px;
    top: 100px;
    width: 408px;
    height: 396px;
    display: flex;
    align-items: center;
    justify-content: flex-end;
    gap: 16px;
  }
  .brand-square {
    width: 36px;
    height: 36px;
    background: var(--silver);
    flex: none;
  }
  .brand-name {
    margin: 0;
    font-size: 27px;
    line-height: 36px;
    font-weight: 600;
    color: var(--text-white);
    white-space: nowrap;
  }
  .tagline {
    position: absolute;
    right: 54px;
    top: 530px;
    margin: 0;
    font-size: 21px;
    line-height: 30px;
    font-style: italic;
    color: var(--text-soft);
  }
</style>
</head>
<body>
  <main class="business-card">
    <h1 class="holder-name">GORDON PELLBURY</h1>
    <p class="holder-role">Managing Director</p>

    <address class="office-address">
      58 Lindmoor Court, Hatherley Road,<br>
      Bristol, BS32 9QJ
    </address>

    <ul class="contact-list">
      <li class="contact-item">
        <svg class="contact-icon" viewBox="0 0 20 20" aria-hidden="true">
          <path d="M2 7c0-2 3-4 8-4s8 2 8 4v1.5h-4V6.5c-1-.6-2.4-.9-4-.9s-3 .3-4 .9v2H2z"/>
          <path d="M5 10h10l2 7H3z M8 12.5a2 2 0 1 0 4 0a2 2 0 1 0-4 0z"/>
        </svg>
        <span>07823 906417</span>
      </li>
      <li class="contact-item">
        <svg class="contact-icon" viewBox="0 0 20 20" aria-hidden="true">
          <path d="M6 1h8a1.5 1.5 0 0 1 1.5 1.5v15A1.5 1.5 0 0 1 14 19H6a1.5 1.5 0 0 1-1.5-1.5v-15A1.5 1.5 0 0 1 6 1zm.5 2.5v11h7v-11zM10 15.6a1 1 0 1 0 0 2a1 1 0 1 0 0-2z"/>
        </svg>
        <span>0117 486 7132</span>
      </li>
      <li class="contact-item">
        <svg class="contact-icon" viewBox="0 0 20 20" aria-hidden="true">
          <path d="M2 5h16v10H2zm1.5 1.2v.4L10 11l6.5-4.4v-.4z"/>
        </svg>
        <span>gordon@fennickexecutive.co.uk</span>
      </li>
      <li class="contact-item">
        <svg class="contact-icon" viewBox="0 0 20 20" aria-hidden="true">
          <circle cx="10" cy="10" r="8" fill="none" stroke="#ffffff" stroke-width="1.8"/>
          <path d="M2 10h16M10 2c-3 3-3 13 0 16M10 2c3 3 3 13 0 16" fill="none" stroke="#ffffff" stroke-width="1.4"/>
        </svg>
        <span>fennickexecutive.co.uk</span>
      </li>
    </ul>

    <div class="brand-block">
      <span class="brand-square" aria-hidden="true"></span>
      <p class="brand-name">Fennick Executive Search</p>
    </div>

    <p class="tagline">Exclusively Sourcing &amp; Hiring Senior Leaders</p>
  </main>
</body>
</html>
```